Homeopathic medicinal cream label design

I am looking for a product label design for a medicinal (cannabis) topical cream to be sold to medical marijuana patients. It is a new product that has not yet established a brand identity. It will be sold in 2 and 4 ounce containers so the design needs to work on a small scale. The design may be used for other branding as well.

Target Market(s)

Medical marijuana users in states where it is legal. The product should appeal to both men and women to promote pain relief in muscles and joints. It can also be used as a massage cream for general relaxation.

Industry/Entity Type

Medical

Font styles to use
Sans Serif

Requirements
Must have
• Something that reflects the company name - The Quiet Heron - and the name of the initial product - Meadow Balm Blend.
• In addition to the name of the company and the name of the product, other information to include would be the volume being sold (e.g. 4 oz.), that it is a topical botanical ointment, and its ingredients (coconut oil, beeswax, soy lecithin, and eight all natural botanical oils - cannabis, lavender, eucalyptus, peppermint, rosemary, cinnamon, clove, and lemon). The label should clearly state that the product is for topical use only.
• The information must fit on the space available on the package. The 4 oz. container's lid has approximately 2 1/8" of surface area. The width of the label on the lid should be approximately 1 7/8". On the container's body, the height of the surface area is approximately 1", and the width is approximately 8 1/2 inches. The width of the label should be around 8 inches to allow room for it to be applied to the container. I have posted a photo of the 4 oz. container and the 2 oz. container. I have also posted a photo of the labeling of some of our competitors with similar products.
Nice to have
• We are thinking of having the logo on the lid of the container, and a circle bordering the lid that may have text in it. (See the "Amber Moth" label attached as an exemplar).
• The label on the body of the container (or maybe on the bottom on the container) would list other information about the product, such as its ingredients and our contact information.

```html
<!DOCTYPE html>
<html lang="en">
<head>
<meta charset="utf-8">
<title>Meadow Balm Blend – Label</title>
<link rel="stylesheet" href="https://fonts.googleapis.com/css2?family=Open+Sans:wght@400;600;700&family=Ubuntu:wght@500&display=swap">
<style>
  :root {
    --paper: #ffffff;
    --rim-brown: #3a2e0c;
    --ring-green: #134a22;
    --olive: #6b7520;
    --olive-light: #8a9530;
    --lime-band: #cde01c;
    --title-ink: #3a3a12;
    --panel-grey: #f2f2f2;
    --panel-line: #c9c9a8;
    --copy-green: #1e5a24;
    --heading-green: #2d6a2a;
    --center-top: #62bd2c;
    --center-bottom: #2e8624;
    --white: #ffffff;
  }
  * { box-sizing: border-box; margin: 0; padding: 0; }
  html, body {
    width: 1200px; height: 913px; overflow: hidden;
    background: var(--paper);
    font-family: "Open Sans", Arial, sans-serif;
  }
  .canvas { position: relative; width: 1200px; height: 913px; }

  /* Lid label */
  .lid-seal { position: absolute; left: 120px; top: 78px; width: 388px; height: 388px; }

  /* Body wrap label */
  .body-label {
    position: absolute; left: 142px; top: 532px; width: 934px; height: 294px;
    border-top: 7px solid var(--rim-brown);
    border-bottom: 7px solid var(--rim-brown);
    border-left: 1px solid var(--panel-line);
    border-right: 1px solid var(--panel-line);
    display: flex;
  }
  .panel { height: 100%; position: relative; }
  .panel-info, .panel-instructions { background: var(--panel-grey); color: var(--copy-green); }
  .panel-info { width: 271px; padding: 18px 10px 0 8px; }
  .panel-instructions { width: 292px; padding: 18px 12px 0 14px; }
  .panel-center {
    width: 371px;
    background: linear-gradient(180deg, var(--center-top), var(--center-bottom));
  }
  .leaf-wash {
    position: absolute; border-radius: 50%;
    background: radial-gradient(ellipse at center, rgba(120,140,80,0.28), rgba(120,140,80,0) 70%);
  }
  .panel-info .leaf-wash { left: 20px; top: 90px; width: 240px; height: 90px; }
  .panel-instructions .leaf-wash { left: 20px; top: 120px; width: 260px; height: 90px; }
  .copy { position: relative; font-size: 13.5px; line-height: 1.42; }
  .copy strong { font-weight: 700; }
  .section-heading {
    position: relative; font-size: 16px; font-weight: 400; color: var(--heading-green);
    margin: 26px 0 4px;
  }
  .panel-instructions .section-heading { margin: 0 0 14px; color: var(--copy-green); font-size: 16px; }

  .body-seal { position: absolute; left: 64px; top: 15px; width: 256px; height: 256px; }
  .topical-note {
    position: absolute; left: 8px; top: 210px; width: 84px;
    color: var(--white); font-size: 13.5px; font-weight: 700; line-height: 1.2; text-align: center;
  }
  .producer-note {
    position: absolute; right: 14px; bottom: 12px;
    color: var(--white); font-size: 10px; font-weight: 700; line-height: 1.25;
  }

  .seal-title { font-family: "Ubuntu", "Open Sans", sans-serif; font-weight: 500; fill: var(--title-ink); }
  .seal-brand { font-family: "Ubuntu", "Open Sans", sans-serif; font-weight: 500; fill: var(--white); }
  .seal-size { font-family: "Open Sans", Arial, sans-serif; font-weight: 700; fill: var(--white); }
</style>
</head>
<body>
<main class="canvas">

  <svg class="lid-seal" viewBox="0 0 400 400" aria-label="Meadow Balm Blend lid label">
    <defs>
      <radialGradient id="leafTone" cx="50%" cy="40%" r="60%">
        <stop offset="0%" stop-color="var(--olive-light)"/>
        <stop offset="100%" stop-color="var(--olive)"/>
      </radialGradient>
      <clipPath id="innerDisc"><circle cx="200" cy="200" r="158"/></clipPath>
    </defs>
    <circle cx="200" cy="200" r="200" fill="var(--rim-brown)"/>
    <circle cx="200" cy="200" r="186" fill="var(--ring-green)"/>
    <g clip-path="url(#innerDisc)">
      <rect x="0" y="0" width="400" height="400" fill="url(#leafTone)" role="img" aria-label="Scattered botanical leaf pattern"/>
      <rect x="0" y="143" width="400" height="111" fill="var(--lime-band)"/>
    </g>
    <text class="seal-title" x="200" y="193" font-size="50" text-anchor="middle">Meadow</text>
    <text class="seal-title" x="200" y="243" font-size="50" text-anchor="middle">Balm Blend</text>
    <circle cx="128" cy="298" r="7" fill="var(--white)"/>
    <text class="seal-brand" x="210" y="304" font-size="22" text-anchor="middle">the quiet heron</text>
    <text class="seal-size" x="200" y="372" font-size="22" text-anchor="middle">4 oz</text>
  </svg>

  <section class="body-label">
    <div class="panel panel-info">
      <div class="leaf-wash" role="img" aria-label="Faint botanical leaf pattern"></div>
      <p class="copy"><strong>Meadow Balm Blend</strong> is Lorem ipsum dolor sit amet, consectetur adipiscing elit. Praesent accumsan, risus non dapibus consequat, mauris est bibendum tellus, in aliquam elit nisl at diam.</p>
      <h2 class="section-heading">Ingredients :</h2>
      <p class="copy">coconut oil, beeswax, soy lecithin, and eight all natural botanical oils - cannabis, lavender, eucalyptus, peppermint, rosemary, cinnamon, clove, and lemon</p>
    </div>

    <div class="panel panel-center">
      <svg class="body-seal" viewBox="0 0 400 400" aria-label="Meadow Balm Blend seal">
        <defs>
          <radialGradient id="leafToneSmall" cx="50%" cy="40%" r="60%">
            <stop offset="0%" stop-color="var(--olive-light)"/>
            <stop offset="100%" stop-color="var(--olive)"/>
          </radialGradient>
          <clipPath id="innerDiscSmall"><circle cx="200" cy="200" r="158"/></clipPath>
        </defs>
        <circle cx="200" cy="200" r="200" fill="var(--rim-brown)"/>
        <circle cx="200" cy="200" r="186" fill="var(--ring-green)"/>
        <g clip-path="url(#innerDiscSmall)">
          <rect x="0" y="0" width="400" height="400" fill="url(#leafToneSmall)" role="img" aria-label="Scattered botanical leaf pattern"/>
          <rect x="0" y="143" width="400" height="111" fill="var(--lime-band)"/>
        </g>
        <text class="seal-title" x="200" y="193" font-size="50" text-anchor="middle">Meadow</text>
        <text class="seal-title" x="200" y="243" font-size="50" text-anchor="middle">Balm Blend</text>
        <circle cx="128" cy="298" r="7" fill="var(--white)"/>
        <text class="seal-brand" x="210" y="304" font-size="22" text-anchor="middle">the quiet heron</text>
        <text class="seal-size" x="200" y="372" font-size="24" text-anchor="middle">4 oz</text>
      </svg>
      <p class="topical-note">for topical use only</p>
      <p class="producer-note">Produced by<br>The Quiet Heron LLC</p>
    </div>

    <div class="panel panel-instructions">
      <div class="leaf-wash" role="img" aria-label="Faint botanical leaf pattern"></div>
      <h2 class="section-heading">Instruction :</h2>
      <p class="copy">Lorem ipsum dolor sit amet, consectetur adipiscing elit. Praesent accumsan, risus non dapibus consequat, mauris est bibendum tellus, in aliquam elit nisl at diam. Curabitur ac viverra dui. Maecenas quis nulla interdum, varius massa sit amet, congue est. Cras purus nulla, pharetra vel consequat at, mattis sit amet justo. Sed lacinia ex eget augue porttitor iaculis. Vestibulum et lectus ac dolor ullamcorper feugiat.</p>
    </div>
  </section>

</main>
</body>
</html>
```